" Atendo como dermatologista em clínicas mas não posso ainda divulgar a especialidade pois ainda não completei a pós graduacao. Preciso de um cartão visita que remeta a pele/beleza/saúde/rejuvenescimento de forma discreta. "

```html
<!DOCTYPE html>
<html lang="pt-BR">
<head>
<meta charset="UTF-8">
<title>Cartão de visitas — Dra. Helena Vasconti</title>
<link rel="stylesheet" href="https://fonts.googleapis.com/css2?family=Cinzel:wght@400;500&family=Open+Sans:wght@400&display=swap">
<style>
  :root {
    --stage: #2b2b2b;
    --card-dark: #0b0b0b;
    --card-dark-edge: #1c1c1c;
    --card-light: #ffffff;
    --gold: #c9a464;
    --gold-light: #e6cf9c;
    --silver: #b9b9b9;
    --silver-light: #e4e4e4;
    --ink: #3a3a3a;
    --ivory: #f2f2f2;
  }
  * { margin: 0; padding: 0; box-sizing: border-box; }
  html, body { width: 1200px; height: 1200px; overflow: hidden; }
  body {
    background: var(--stage);
    position: relative;
    font-family: "Open Sans", Arial, sans-serif;
  }
  .card {
    position: absolute;
    top: 450px;
    width: 540px;
    height: 300px;
    overflow: hidden;
  }
  .card--front {
    left: 45px;
    background: radial-gradient(ellipse at 50% 40%, var(--card-dark-edge), var(--card-dark) 75%);
  }
  .card--back {
    left: 615px;
    background: var(--card-light);
  }

  /* front */
  .front__mark {
    position: absolute;
    top: 78px; left: 0; width: 100%;
    text-align: center;
    font-family: "Cinzel", Georgia, serif;
    font-size: 40px;
    color: var(--gold);
    letter-spacing: 1px;
  }
  .front__name {
    position: absolute;
    top: 136px; left: 0; width: 100%;
    text-align: center;
    font-family: "Cinzel", Georgia, serif;
    font-size: 28px;
    color: var(--ivory);
    letter-spacing: 2px;
  }
  .front__role {
    position: absolute;
    top: 178px; left: 0; width: 100%;
    display: flex; justify-content: center; align-items: center; gap: 10px;
    font-family: "Cinzel", Georgia, serif;
    font-size: 11px;
    color: var(--gold);
    letter-spacing: 1.5px;
  }
  .front__role::before, .front__role::after {
    content: ""; width: 40px; height: 1px; background: var(--gold);
  }
  .front__swoosh { position: absolute; left: 0; bottom: 0; width: 540px; height: 90px; }

  /* back */
  .back__mark {
    position: absolute;
    top: 30px; left: 18px;
    font-family: "Cinzel", Georgia, serif;
    font-size: 190px;
    line-height: 1;
    color: var(--silver-light);
  }
  .back__name {
    position: absolute;
    top: 30px; right: 26px;
    text-align: right;
    font-family: "Cinzel", Georgia, serif;
    font-size: 22px;
    line-height: 1.2;
    color: var(--gold);
    letter-spacing: 0.5px;
  }
  .contact-list {
    position: absolute;
    top: 118px; right: 26px;
    list-style: none;
    text-align: right;
    font-size: 11.5px;
    color: var(--ink);
  }
  .contact-list__item {
    display: flex; justify-content: flex-end; align-items: center; gap: 7px;
    margin-bottom: 15px;
  }
  .contact-list__item--address { align-items: flex-start; line-height: 1.4; }
  .contact-list__icon { width: 11px; height: 11px; flex: none; fill: var(--gold); }
  .contact-list__item--address .contact-list__icon { margin-top: 3px; }
</style>
</head>
<body>

  <section class="card card--front">
    <div class="front__mark">HV</div>
    <h1 class="front__name">Dra. Helena Vasconti</h1>
    <p class="front__role">Médica / CRMMG 48213</p>
    <svg class="front__swoosh" viewBox="0 0 540 90" preserveAspectRatio="none" aria-hidden="true">
      <defs>
        <linearGradient id="goldBand" x1="0" x2="1">
          <stop offset="0" stop-color="#6b5430"/>
          <stop offset="0.5" stop-color="#e6cf9c"/>
          <stop offset="1" stop-color="#b08a4c"/>
        </linearGradient>
        <linearGradient id="silverBand" x1="0" x2="1">
          <stop offset="0" stop-color="#8a8a8a"/>
          <stop offset="0.5" stop-color="#f2f2f2"/>
          <stop offset="1" stop-color="#a9a9a9"/>
        </linearGradient>
      </defs>
      <path d="M0 62 C160 66 360 58 540 44 L540 52 C360 68 160 74 0 72 Z" fill="url(#goldBand)"/>
      <path d="M0 76 C180 78 380 70 540 58 L540 90 L0 90 Z" fill="url(#silverBand)"/>
      <path d="M0 84 C180 86 380 80 540 72 L540 90 L0 90 Z" fill="#d6d6d6"/>
    </svg>
  </section>

  <section class="card card--back">
    <div class="back__mark">HV</div>
    <h2 class="back__name">Dra. Helena Duarte<br>Vasconti</h2>
    <ul class="contact-list">
      <li class="contact-list__item">(31) 9.9512-0048
        <svg class="contact-list__icon" viewBox="0 0 12 12" aria-hidden="true"><path d="M2.5 1 L4.5 1 L5.2 3.6 L4 4.6 C4.6 6 6 7.4 7.4 8 L8.4 6.8 L11 7.5 L11 9.5 C11 10.4 10.4 11 9.5 11 C5 11 1 7 1 2.5 C1 1.6 1.6 1 2.5 1 Z"/></svg>
      </li>
      <li class="contact-list__item">@drahelenavasconti
        <svg class="contact-list__icon" viewBox="0 0 12 12" aria-hidden="true"><circle cx="6" cy="6" r="5.5"/></svg>
      </li>
      <li class="contact-list__item">helena.vasconti@email.com
        <svg class="contact-list__icon" viewBox="0 0 12 12" aria-hidden="true"><path d="M0.5 2.5 H11.5 V9.5 H0.5 Z M1 3 L6 6.6 L11 3" fill="none" stroke="#c9a464" stroke-width="1"/></svg>
      </li>
      <li class="contact-list__item contact-list__item--address"><span>End. completo, 00, Bairro<br>CEP 0000.000 - Cidade-SP</span>
        <svg class="contact-list__icon" viewBox="0 0 12 12" aria-hidden="true"><path d="M6 0.5 C3.8 0.5 2.2 2.1 2.2 4.2 C2.2 7 6 11.5 6 11.5 C6 11.5 9.8 7 9.8 4.2 C9.8 2.1 8.2 0.5 6 0.5 Z M6 2.8 A1.4 1.4 0 1 1 6 5.6 A1.4 1.4 0 1 1 6 2.8 Z" fill-rule="evenodd"/></svg>
      </li>
    </ul>
  </section>

</body>
</html>
```